Landing Page für Beratungszentrum
Zielgruppe
Benötige für ein 'Kornfeld-Beratungszentrum Bau- und Immobilienökonomie' zunächst eine Landing-Page mit Einbindung 'Sachverständiger DIN EN ISO/IEC 17024 für Wertermittlung und Baukostenermittlung und -abrechnung sowie Bauablaufstörung ZERTANO 7-58-4096' sowie Link auf Hochschule (https://www.lxa-campus.de/hochschule/lehrende/ostrander-matthias/)
Nachfolgende Info gemäss Links.
https://www.kornfeld-netz.de/su/7391
https://www.kornfeld-netz.de/de/aktuelles/gruendung-kornfeld-unternehmen.html
Aufgabenstellung
Das Corporate Design von Kornfeld sollte im wesentlichen eingehalten werden. Es gibt ein Logo (beiliegend). Es gibt noch keine eigene Domain (muss noch erfunden werden www.kornfeld-bauoek.xxx; email gibt es matthias.ostrander@kfv-mail.de); rudimentäres Web/Domain Architekt gibt es (moplan.net über webtara). Bild/Bilder nach Abstimmung. Info/Leistungen muss textlich bereinigt werden.
Ein Manual Kornfeld gibt es nicht, nur einige Hinweise im Leitfaden Unternehmenskommunikation (Punkt 7.3, als PDF anbei).

```html
<!DOCTYPE html>
<html lang="de">
<head>
<meta charset="utf-8">
<title>Kornfeld-Beratungszentrum Bau- und Immobilienökonomie</title>
<link rel="stylesheet" href="https://fonts.googleapis.com/css2?family=Barlow:wght@400;500;600;700&family=Barlow+Semi+Condensed:wght@400&display=swap">
<style>
:root{
  --navy:#0c2238;
  --navy-deep:#0a1e31;
  --teal:#45b8d3;
  --teal-text:#3aa6c7;
  --cert-bg:#e8f3f5;
  --cert-line:#6fb3c7;
  --light:#f4f6f8;
  --ink:#0d1a26;
  --white:#ffffff;
}
*{margin:0;padding:0;box-sizing:border-box}
html,body{width:821px;height:1200px;overflow:hidden}
body{font-family:"Barlow",sans-serif;color:var(--ink);background:var(--white);position:relative}
a{color:inherit;text-decoration:none}

.site-header{position:absolute;top:0;left:0;width:821px;height:54px}
.brand{position:absolute;left:130px;top:18px;display:flex;align-items:center;gap:5px}
.brand-mark{width:18px;height:18px;border:2px solid var(--ink)}
.brand-name{font-weight:600;font-size:9px;line-height:9.5px;white-space:nowrap}
.main-nav{position:absolute;right:130px;top:21px;display:flex;align-items:center;gap:21px;font-size:7.5px;font-weight:600}
.nav-cta{background:var(--navy);color:var(--white);padding:4px 6px;border-radius:3px}

.hero{position:absolute;top:54px;left:0;width:821px;height:260px;display:flex}
.hero-text{width:410px;background:var(--navy);color:var(--white);padding:61px 0 0 130px}
.hero-title{font-size:26px;line-height:29px;font-weight:700}
.hero-lead{margin-top:14px;font-family:"Barlow Semi Condensed",sans-serif;font-size:7px;line-height:12px;width:236px}
.hero-photo{flex:1;background:linear-gradient(135deg,#2d3b4c 0%,#5b6f85 45%,#c7d5de 70%,#3e4d5e 100%)}

.cert{position:absolute;top:329px;left:128px;width:565px;height:43px;background:var(--cert-bg);border:1px solid var(--cert-line);display:flex;align-items:center;justify-content:center;gap:7px;font-size:7.8px;line-height:11px;font-weight:500}

.about{position:absolute;top:388px;left:128px;width:565px;height:262px;display:flex;background:var(--light)}
.about-photo{width:305px;background:linear-gradient(90deg,#a9cfea 0%,#c6e0f2 45%,#2a2f38 58%,#b6b1aa 80%,#8b8780 100%)}
.about-body{padding:22px 0 0 33px;width:240px}
.section-title{font-size:14px;font-weight:700;letter-spacing:.2px}
.about-text{margin-top:10px;font-size:7.8px;line-height:13.7px;width:207px}
.about-text + .about-text{margin-top:13px}
.btn-small{display:inline-block;margin-top:11px;background:var(--navy);color:var(--white);font-size:7px;font-weight:600;padding:4px 7px;border-radius:2px}

.services{position:absolute;top:672px;left:128px;width:565px}
.service-grid{margin-top:13px;display:flex;gap:5px}
.service-card{width:137px;height:106px;background:var(--navy);border-radius:3px;color:var(--white);display:flex;flex-direction:column;align-items:center;padding-top:19px;text-align:center}
.service-card svg{width:30px;height:30px}
.service-name{margin-top:13px;font-size:7px;line-height:10.5px;font-weight:600}

.contact{position:absolute;top:831px;left:128px;width:565px;height:92px;background:var(--light);text-align:center;padding-top:14px}
.contact-buttons{margin-top:13px;display:flex;gap:6px;justify-content:center}
.contact-btn{width:175px;height:28px;background:var(--teal);color:var(--white);border-radius:2px;display:flex;align-items:center;justify-content:center;gap:6px;font-size:9.5px;font-weight:600}

.site-footer{position:absolute;top:973px;left:0;width:821px;height:227px;background:var(--navy-deep)}
.footer-cols{position:absolute;left:101px;top:18px;display:flex}
.footer-col{width:133px}
.footer-col h3{color:var(--teal-text);font-size:9px;font-weight:600;margin-bottom:8px}
.footer-col h3.spaced{margin-top:20px}
.footer-col li{list-style:none;color:#b9c4cf;font-size:7px;line-height:11.6px}
.footer-bar{position:absolute;left:0;top:177px;width:821px;height:50px;border-top:1px solid #16324a}
.legal{position:absolute;left:101px;top:16px;width:310px;color:var(--teal-text);font-size:7px;line-height:11.5px}
.legal span{margin-right:5px}
.social{position:absolute;right:72px;top:16px;display:flex;gap:9px;color:var(--teal-text);font-size:7px;font-weight:600}
</style>
</head>
<body>

<header class="site-header">
  <a class="brand" href="#"><span class="brand-mark"></span><span class="brand-name">Kornfeld-Beratungszentrum<br>Bau- und Immobilienökonomie</span></a>
  <nav class="main-nav">
    <a href="#">Start</a><a href="#">About</a><a href="#">Leistungen</a><a class="nav-cta" href="#">Kontakt aufnehmen</a>
  </nav>
</header>

<section class="hero">
  <div class="hero-text">
    <h1 class="hero-title">Beratung für Bau- &amp; Immobilienökonomie</h1>
    <p class="hero-lead">Lorem ipsum dolor sit amet, consetetur sadipscing elitr, sed diam nonumy eirmod tempor invidunt ut labore et dolore magna aliquyam erat, sed diam voluptua. At vero eos et accusam et justo duo dolores et ea rebum. Stet clita kasd gubergren, no sea takimata sanctus es</p>
  </div>
  <div class="hero-photo" role="img" aria-label="Foto: Hand mit Kugelschreiber unterschreibt ein Dokument auf einem Tisch"></div>
</section>

<section class="cert">
  <svg width="17" height="20" viewBox="0 0 17 20" aria-hidden="true"><path d="M8.5 1 L15.5 3.5 V9.5 C15.5 14 12.5 17 8.5 19 C4.5 17 1.5 14 1.5 9.5 V3.5 Z" fill="none" stroke="#3aa6c7" stroke-width="1.6"/><path d="M5 10 L7.7 12.6 L12.2 7.6" fill="none" stroke="#3aa6c7" stroke-width="1.6"/></svg>
  <p>Sachverständiger DIN EN ISO/IEC 17024 für Wertermittlung<br>und Baukostenermittlung und -abrechnung sowie Bauablaufstörung ZERTANO 7-58-4096</p>
</section>

<section class="about">
  <div class="about-photo" role="img" aria-label="Foto: Hochhausfassade von unten vor blauem Himmel mit Vögeln"></div>
  <div class="about-body">
    <h2 class="section-title">ABOUT</h2>
    <p class="about-text">Matthias Ostrander, Architekt und promovierter Wirtschafts- und Managementexperte, verfügt über langjährige Erfahrung im Immobilien- und Bauwesen im DACH-Raum. Er hatte Führungsrollen in Joint Ventures mit Unternehmen wie Hartmann &amp; Reis, Veltrion und NBV inne und leitete große Multi-Stakeholder-Projekte.</p>
    <p class="about-text">Als Gutachter und Spezialist für Risk Engineering war er zudem langjähriger Dozent an der Hochschule Seeburg, u. a. für nachhaltiges Bauen und Spitalbau. Prof. Dr. Ostrander ist unternehmerisch tätig und Mitglied verschiedener Gremien im In- und Ausland.</p>
    <a class="btn-small" href="https://www.lxa-campus.de/hochschule/lehrende/ostrander-matthias/">Zum Kurzprofil</a>
  </div>
</section>

<section class="services">
  <h2 class="section-title">LEISTUNGEN</h2>
  <div class="service-grid">
    <div class="service-card">
      <svg viewBox="0 0 30 30" fill="none" stroke="#45b8d3" stroke-width="2.2"><path d="M1 16 L7 8 L11 14 L15 6 L19 12 L27 2"/><circle cx="19" cy="20" r="5"/><path d="M23 24 L28 29"/></svg>
      <p class="service-name">WIRTSCHAFTLICHKEITS-<br>ANALYSE &amp; -STRATEGIE</p>
    </div>
    <div class="service-card">
      <svg viewBox="0 0 30 30" fill="none" stroke="#45b8d3" stroke-width="2.2"><path d="M10 12 L19 5 L27 11 V23"/><path d="M2 16 H9 L17 19 H22 L27 23 L14 27 H2 Z"/><rect x="17" y="11" width="3" height="3" stroke-width="1.2"/></svg>
      <p class="service-name">PORTFOLIO- &amp; ASSET-<br>MANAGEMENT</p>
    </div>
    <div class="service-card">
      <svg viewBox="0 0 30 30" fill="none" stroke="#45b8d3" stroke-width="2.2"><circle cx="15" cy="5" r="3"/><path d="M15 8 V24 M15 16 L6 21 M15 16 L24 21"/><circle cx="5" cy="23" r="3"/><circle cx="15" cy="26" r="3"/><circle cx="25" cy="23" r="3"/></svg>
      <p class="service-name">NACHHALTIGKEITS- &amp;<br>LEBENSZYKLUSANALYSE</p>
    </div>
    <div class="service-card">
      <svg viewBox="0 0 30 30" fill="none" stroke="#45b8d3" stroke-width="2.2"><path d="M2 9 L14 3 L26 9 Z M3 11 H25 M6 13 V22 M12 13 V22 M2 26 H17"/><path d="M23 17 L28 19 V22 C28 25 26 27 23 28 C20 27 18 25 18 22 V19 Z" fill="#45b8d3" stroke="none"/></svg>
      <p class="service-name">PROJEKTENTWICKLUNG &amp;<br>FINANZIERUNG</p>
    </div>
  </div>
</section>

<section class="contact">
  <h2 class="section-title">KONTAKT</h2>
  <div class="contact-buttons">
    <a class="contact-btn" href="mailto:matthias.ostrander@kfv-mail.de"><svg width="11" height="8" viewBox="0 0 11 8" fill="none" stroke="#fff" stroke-width="1"><rect x=".5" y=".5" width="10" height="7"/><path d="M.5 .5 L5.5 4.5 L10.5 .5"/></svg>E-MAIL SCHREIBEN</a>
    <a class="contact-btn" href="#">LINKORA</a>
    <a class="contact-btn" href="#">ZINGO</a>
  </div>
</section>

<footer class="site-footer">
  <div class="footer-cols">
    <div class="footer-col"><h3>Kornfeld</h3><ul><li>Über Kornfeld</li><li>Historie</li><li>Kuratorium</li><li>Dienstleistungen</li><li>Struktur</li><li>Transferpreis</li><li>Kornfeld-Auszeichnung</li><li>Karriere</li></ul></div>
    <div class="footer-col"><h3>Verbund</h3><ul><li>Suche im Kornfeld-Verbund</li><li>Anton-Kornfeld-Gesellschaft</li><li>Kornfeld-Kooperationen mit</li><li>Hochschulen</li><li>Kornfeld regional</li><li>Netzwerk Gründerwerk Talheim</li><li>Kornfeld weltweit</li><li>Neubau Kornfeld-Haus</li><li>Lindach</li><li>Neubau Kornfeld-Haus Berlin</li></ul></div>
    <div class="footer-col"><h3>Publikationen</h3><ul><li>Transfer-Magazin</li><li>Unternehmenspublikationen</li><li>Kornfeld-Studien</li><li>Kornfeld-Edition</li><li>KornfeldART</li></ul></div>
    <div class="footer-col"><h3>Veranstaltungen</h3><ul><li>Kornfeld-Campus-Event</li><li>Kornfeld Engineering Tag</li><li>Kornfeld-Dialog Forum</li><li>#wissenbaut</li><li>Technik*Erleben</li><li>Paul Brenner-Symposium</li><li>Neue Wege im</li><li>Innovieren</li><li>Kornfeld Lunchbreak</li><li>Newsletter-Anmeldung</li></ul></div>
    <div class="footer-col"><h3>Aktuelles</h3><h3 class="spaced">Mediathek</h3><ul><li>Videos</li><li>Publikationen</li></ul></div>
  </div>
  <div class="footer-bar">
    <p class="legal"><span>Kontakt</span><span>Impressum</span><span>Der Weg zu uns</span><span>Datenschutz</span><span>Online-Shop</span><span>Hinweisgebersystem</span><br>&nbsp;Lieferkettensorgfaltspflichtengesetz</p>
    <div class="social"><span>Clipra</span><span>Freundo</span><span>Tubio</span><span>Linkora</span><span>Pixgram</span></div>
  </div>
</footer>

</body>
</html>
```